Flat Belly Design Graphics for Social

I want to create 9 social media graphics (new Instagram size 4:5 (1080 x 1350 pixels) focusing on our Flat Belly Graphics, using the pics attached. Use the attached pics, NO RANDOM STOCK PHOTOGRAPHY. For the color scheme of the graphics, the color palette is attached. YOU MUST POST ALL 9 GRAPHICS IN ONE ENTRY.
Using the 3 titles below, create one set of graphics. 1) with all text, then for the others, use the pictures as detailed below in IMPORTANT:
1. 21-Night Lean Middle Reboot Beyond 50
2. The 20-Second Trim-Core Menu Guide
3. Starlet Tricks to a Slender Midline Beyond 50 - Zero Scalpel Needed
IMPORTANT:
Only use RK Pic 1 and RK Pic 2 with the title, 21-Night Lean Middle Reboot Beyond 50
Only use meal plan1 and meal plan2 pics with the title, 20-Second Trim-Core Menu Guide
Only use starlet tricks 1 and starlet tricks 2 pics with the title, Starlet Tricks to a Slender Midline Beyond 50 - Zero Scalpel Needed
women over 40

```html
<!DOCTYPE html>
<html lang="en">
<head>
<meta charset="utf-8">
<title>Lean Middle Reboot &amp; Trim-Core Menu Guide – Social Set</title>
<link rel="stylesheet" href="https://fonts.googleapis.com/css2?family=Poppins:wght@700;800&family=Dancing+Script:wght@600;700&family=Great+Vibes&display=swap">
<style>
  :root{
    --canvas:#f2faf8;
    --pink:#fbcfd4;
    --pink-deep:#f6b3bb;
    --blush:#fde9ec;
    --white:#ffffff;
    --forest:#324d4b;
    --ink:#0d0d0d;
    --rose:#df4f5c;
    --photo-warm:#caa08f;
    --photo-wood:#6b4a35;
    --photo-green:#8fb37a;
  }
  *{margin:0;padding:0;box-sizing:border-box}
  html,body{width:1008px;height:1200px;overflow:hidden;background:var(--canvas)}
  .sheet{position:relative;width:1008px;height:1200px}
  .post{position:absolute;width:432px;height:540px;overflow:hidden;
    background:linear-gradient(90deg,var(--pink) 0%,var(--blush) 55%,var(--white) 100%)}
  .post--tl{left:59px;top:51px}
  .post--tr{left:517px;top:51px}
  .post--bl{left:59px;top:609px}
  .post--br{left:517px;top:609px}
  .post svg.backdrop{position:absolute;inset:0;width:432px;height:540px}
  .label{position:absolute;font-family:"Poppins",sans-serif;font-weight:800;color:var(--ink);white-space:nowrap;line-height:1}
  .ribbon-text{color:var(--white);font-size:28px;font-weight:700;top:59px;left:26px}
  .script{position:absolute;font-family:"Dancing Script",cursive;font-weight:700;color:var(--ink);white-space:nowrap;line-height:1}
  .fancy{font-family:"Great Vibes",cursive;font-weight:400}
  .number{position:absolute;font-family:"Poppins",sans-serif;font-weight:800;color:var(--forest);line-height:1}
  .rose{color:var(--rose)}
  .center{left:0;width:432px;text-align:center}
</style>
</head>
<body>
<main class="sheet">

  <!-- Post 1: program with portrait -->
  <section class="post post--tl">
    <svg class="backdrop" viewBox="0 0 432 540">
      <defs>
        <linearGradient id="blobA" x1="0" y1="0" x2="0" y2="1">
          <stop offset="0" stop-color="#ffffff"/><stop offset="0.6" stop-color="#fbd3d8"/><stop offset="1" stop-color="#f5b2ba"/>
        </linearGradient>
        <linearGradient id="portraitFill" x1="0" y1="0" x2="0" y2="1">
          <stop offset="0" stop-color="#f3d6d6"/><stop offset="0.55" stop-color="var(--photo-warm)"/><stop offset="1" stop-color="#3a2a28"/>
        </linearGradient>
      </defs>
      <path d="M432 50 C300 60 160 150 145 300 C135 380 200 420 300 430 C360 440 400 450 432 460 Z" fill="url(#blobA)" stroke="#f7dce0" stroke-width="3"/>
      <path d="M0 540 L0 320 C120 420 260 420 432 440 L432 540 Z" fill="#fff" opacity=".35"/>
      <path d="M210 90 C250 70 400 80 432 100 L432 400 L390 388 C330 360 270 360 225 360 C190 300 185 180 210 90 Z" fill="url(#portraitFill)" role="img" aria-label="Photo of a smiling woman in a white cropped sweater pointing at her toned midsection"/>
      <path d="M0 474 C20 448 60 444 110 455 C200 475 280 515 346 540 L0 540 Z" fill="var(--forest)"/>
      <path d="M0 45 L262 45 C232 50 192 62 190 73 C192 84 232 96 262 101 L0 101 Z" fill="var(--forest)"/>
    </svg>
    <div class="label ribbon-text">21 NIGHT</div>
    <div class="label" style="left:18px;top:196px;font-size:24px">LEAN MIDDLE</div>
    <div class="script" style="left:14px;width:190px;text-align:center;top:241px;font-size:27px">Reboot Beyond</div>
    <div class="number" style="left:14px;width:190px;text-align:center;top:292px;font-size:70px">50</div>
  </section>

  <!-- Post 2: menu guide with food photo -->
  <section class="post post--tr">
    <svg class="backdrop" viewBox="0 0 432 540">
      <defs>
        <linearGradient id="foodFill" x1="0" y1="0" x2="1" y2="1">
          <stop offset="0" stop-color="var(--photo-green)"/><stop offset="0.45" stop-color="var(--photo-wood)"/><stop offset="1" stop-color="#e9e4dc"/>
        </linearGradient>
      </defs>
      <path d="M0 135 C80 130 200 150 260 190 C300 230 285 330 270 380 C240 450 150 470 0 470 Z" fill="url(#foodFill)" role="img" aria-label="Overhead photo of a meal plan sheet surrounded by fresh vegetables, fruit, nuts and chickpeas"/>
      <path d="M104 455 C180 440 250 420 278 395 C275 440 240 475 178 480 Z" fill="var(--forest)"/>
      <path d="M0 480 C40 490 100 500 170 495 C260 505 340 530 432 525 L432 540 L0 540 Z" fill="#fde7ea"/>
      <circle cx="307" cy="293" r="103" fill="#fff" stroke="#f6d6db" stroke-width="3"/>
      <path d="M0 45 L290 45 C260 50 220 62 218 73 C220 84 260 96 290 101 L0 101 Z" fill="var(--forest)"/>
    </svg>
    <div class="label ribbon-text">20 SECOND</div>
    <div class="label" style="left:192px;top:130px;font-size:34px">TRIM <span class="script fancy" style="position:static;font-size:46px;font-weight:400">Core</span></div>
    <div class="script rose" style="left:204px;width:206px;text-align:center;top:230px;font-size:52px;line-height:1.1">Menu<br>Guide</div>
  </section>

  <!-- Post 3: program, all text -->
  <section class="post post--bl">
    <svg class="backdrop" viewBox="0 0 432 540">
      <path d="M432 50 C300 60 160 150 145 300 C135 380 200 420 300 430 C360 440 400 450 432 460 Z" fill="url(#blobA)" stroke="#f7dce0" stroke-width="3"/>
      <path d="M0 474 C20 448 60 444 110 455 C200 475 280 515 346 540 L0 540 Z" fill="var(--forest)"/>
      <path d="M70 45 L362 45 C332 50 292 62 290 73 C292 84 332 96 362 101 L70 101 C93 92 111 82 111 73 C111 64 93 54 70 45 Z" fill="var(--forest)"/>
    </svg>
    <div class="label center" style="top:59px;font-size:28px;font-weight:700;color:var(--white)">21 NIGHT</div>
    <div class="label center" style="top:155px;font-size:44px">LEAN MIDDLE</div>
    <div class="script center" style="top:235px;font-size:52px">Reboot Beyond</div>
    <div class="number center" style="top:318px;font-size:124px">50</div>
  </section>

  <!-- Post 4: menu guide, all text -->
  <section class="post post--br">
    <svg class="backdrop" viewBox="0 0 432 540">
      <path d="M0 45 L290 45 C260 50 220 62 218 73 C220 84 260 96 290 101 L0 101 Z" fill="var(--forest)"/>
      <line x1="90" y1="364" x2="342" y2="364" stroke="var(--forest)" stroke-width="1"/>
      <circle cx="211" cy="364" r="10" fill="var(--forest)"/>
    </svg>
    <div class="label ribbon-text">20 SECOND</div>
    <div class="label center" style="top:176px;font-size:34px">TRIM <span class="script fancy" style="position:static;font-size:46px;font-weight:400">Core</span></div>
    <div class="script rose center" style="top:232px;font-size:78px">Menu Guide</div>
  </section>

</main>
</body>
</html>
```